Antibacterial Hand Wash Squeeze Tube Label

We're looking for a contemporary label design for a new Antibacterial Hand Wash for an 8oz squeeze tube. The new consumer brand will be sold to consumers in major US retail stores & online. The moisturizing hand wash contains Aloe Vera, vitamin E, and other natural ingredients so the design should include the color green. Real photos are very effective on packaging, so a picture of Aloe Vera or possibly two hands washing would help draw consumers' attention to the tube on the retail shelf. The front label may wrap around the sides. Rear must be left mostly blank
US Consumers - retail stores & online
Consumer

```html
<!DOCTYPE html>
<html lang="en">
<head>
<meta charset="utf-8">
<title>Moisturizing Hand Wash Label</title>
<link href="https://fonts.googleapis.com/css2?family=Jost:wght@400;500;600;700&display=swap" rel="stylesheet">
<style>
  :root {
    --backdrop: #dcdcdc;
    --label-white: #ffffff;
    --leaf-green: #8dc63f;
    --leaf-green-light: #a8d65c;
    --leaf-green-deep: #5fa82a;
    --charcoal: #3f3f3f;
    --text-grey: #4a4a4a;
    --skin-light: #f1d3c6;
    --skin-mid: #e2b2a0;
  }
  * { margin: 0; padding: 0; box-sizing: border-box; }
  html, body {
    width: 1200px; height: 948px; overflow: hidden;
    background: var(--backdrop);
    font-family: "Jost", sans-serif;
  }
  .label {
    position: absolute; left: 376px; top: 34px;
    width: 448px; height: 880px;
    background: var(--label-white);
    overflow: hidden;
  }
  .aloe-photo {
    position: absolute; left: -40px; top: 20px; width: 300px; height: 250px;
    background: radial-gradient(ellipse 60% 55% at 45% 45%, var(--leaf-green-light) 0%, var(--leaf-green) 45%, rgba(95,168,42,0.55) 70%, rgba(141,198,63,0) 100%);
  }
  .hands-photo {
    position: absolute; left: 176px; top: 525px; width: 290px; height: 220px;
    background: radial-gradient(ellipse 58% 48% at 62% 48%, var(--skin-light) 0%, var(--skin-mid) 55%, rgba(226,178,160,0) 100%);
  }
  .headline {
    position: absolute; left: 0; top: 0; width: 448px; height: 520px;
    font-family: "Jost", sans-serif;
  }
  .headline .tagline { font-size: 26px; font-weight: 400; fill: var(--leaf-green); }
  .headline .title { font-size: 102px; font-weight: 600; }
  .headline .title-hand { fill: var(--charcoal); }
  .headline .title-wash { fill: var(--leaf-green); }
  .headline .sub-with { font-size: 20px; font-weight: 400; fill: var(--text-grey); }
  .headline .sub-aloe { font-size: 20px; font-weight: 600; fill: var(--leaf-green); }
  .features { position: absolute; left: 52px; top: 574px; list-style: none; }
  .feature {
    display: flex; align-items: flex-start; gap: 6px;
    font-size: 17px; color: var(--text-grey); line-height: 21px;
    margin-bottom: 13px;
  }
  .feature svg { width: 31px; height: 31px; flex: none; }
  .feature span { padding-top: 5px; }
  .band-brand {
    position: absolute; left: 0; top: 759px; width: 448px; height: 68px;
    background: linear-gradient(90deg, var(--leaf-green) 0%, var(--leaf-green-light) 60%, var(--leaf-green) 100%);
    display: flex; align-items: center; padding-left: 53px;
    font-size: 18px; color: #1e1e1e;
  }
  .band-brand .brand-by { font-weight: 400; margin-right: 8px; }
  .band-brand .brand-name { font-weight: 600; letter-spacing: 0.5px; }
  .band-size {
    position: absolute; left: 0; top: 827px; width: 448px; height: 53px;
    background: var(--charcoal); color: #fff;
    display: flex; align-items: center; justify-content: center;
    font-size: 18px; font-weight: 600; letter-spacing: 0.5px;
  }
</style>
</head>
<body>
  <main class="label">
    <div class="aloe-photo" role="img" aria-label="Cut aloe vera leaves dripping clear gel"></div>
    <div class="hands-photo" role="img" aria-label="Two soapy hands being washed"></div>

    <svg class="headline" viewBox="0 0 448 520" role="group" aria-label="Moisturizing Hand Wash with Aloe Vera">
      <text class="tagline" x="364" y="255" text-anchor="end">Moisturizing</text>
      <text class="title title-hand" x="77" y="345" textLength="292" lengthAdjust="spacingAndGlyphs">HAND</text>
      <text class="title title-wash" x="77" y="428" textLength="292" lengthAdjust="spacingAndGlyphs">WASH</text>
      <text class="sub-with" x="223" y="469" text-anchor="middle">with</text>
      <text class="sub-aloe" x="221" y="495" text-anchor="middle">Aloe Vera</text>
    </svg>

    <ul class="features">
      <li class="feature">
        <svg viewBox="0 0 32 32" aria-hidden="true">
          <circle cx="16" cy="16" r="14" fill="none" stroke="var(--leaf-green)" stroke-width="2.5"/>
          <circle cx="16" cy="16" r="9.5" fill="var(--leaf-green)"/>
          <circle cx="13" cy="14" r="2" fill="#fff"/>
          <circle cx="19" cy="18.5" r="1.6" fill="#fff"/>
          <line x1="9" y1="23" x2="23" y2="9" stroke="#fff" stroke-width="2"/>
        </svg>
        <span>Antibacterial</span>
      </li>
      <li class="feature">
        <svg viewBox="0 0 32 32" aria-hidden="true">
          <circle cx="16" cy="16" r="14" fill="none" stroke="var(--leaf-green)" stroke-width="2.5"/>
          <circle cx="16" cy="16" r="9.5" fill="var(--leaf-green)"/>
          <path d="M19.5 10.5h-7v11h7M12.5 16h6" fill="none" stroke="#fff" stroke-width="2"/>
        </svg>
        <span>Vitamin E</span>
      </li>
      <li class="feature">
        <svg viewBox="0 0 32 32" aria-hidden="true">
          <circle cx="16" cy="16" r="14" fill="none" stroke="var(--leaf-green)" stroke-width="2.5"/>
          <circle cx="16" cy="16" r="9.5" fill="var(--leaf-green)"/>
          <path d="M16 22v-5M16 17c-4 0-5-3-5-5 3 0 5 1 5 5zM16 17c4 0 5-3 5-5-3 0-5 1-5 5z" fill="#fff" stroke="#fff" stroke-width="1.2"/>
        </svg>
        <span>Natural<br>ingredients</span>
      </li>
    </ul>

    <div class="band-brand">
      <span class="brand-by">BY</span><span class="brand-name">VERDALE</span>
    </div>
    <div class="band-size">8 OZ ( 250 ML )</div>
  </main>
</body>
</html>
```